Small rum distillery looking for bottle design

Small rum distillery in Estonia. Looking for bottle lable design. It should be simple but at the same time point out from the variety of other bottles.
As we are a small nordic country, design can be some how nordic or represent our country. It can also have some connection with sailing or sea as we know it pirates love it.
Bottle we are using is Corvane 540

Industry/Entity Type

food and beverage

Other font styles liked:
• Baskerville

```html
<!DOCTYPE html>
<html lang="en">
<head>
<meta charset="utf-8">
<title>Merevaik Distillery – Rum Labels</title>
<link rel="stylesheet" href="https://fonts.googleapis.com/css2?family=Cinzel:wght@400;500&family=Libre+Baskerville:wght@400&display=swap">
<style>
  :root {
    --sea-blue: #4ab1dd;
    --flag-red: #c0302a;
    --panel-dark: #3b3b3b;
    --panel-light: #a3a3a3;
    --ink: #333333;
    --white: #ffffff;
    --page: #ffffff;
  }
  html, body {
    margin: 0;
    padding: 0;
    width: 1200px;
    height: 2800px;
    overflow: hidden;
    background: var(--page);
  }
  .canvas {
    position: relative;
    width: 1200px;
    height: 2800px;
  }
  .label {
    position: absolute;
    left: 146px;
    width: 932px;
    height: 1197px;
  }
  .label--blue { top: 132px; --accent: var(--sea-blue); }
  .label--red  { top: 1416px; --accent: var(--flag-red); }
  .label svg { display: block; width: 100%; height: 100%; }
  .accent-fill { fill: var(--accent); }
  .oval-frame { fill: none; stroke: var(--white); }
  .brand-name {
    font-family: "Cinzel", serif;
    font-weight: 400;
    font-size: 25px;
    letter-spacing: 1.5px;
    fill: var(--white);
  }
  .brand-sub {
    font-family: "Cinzel", serif;
    font-weight: 400;
    font-size: 8.5px;
    letter-spacing: 3.2px;
    fill: var(--white);
  }
  .spec {
    font-family: "Libre Baskerville", serif;
    font-size: 8.5px;
    fill: var(--ink);
  }
  .origin-line {
    font-family: "Libre Baskerville", serif;
    font-size: 9.6px;
    fill: var(--white);
  }
  .origin-line .origin-country { fill: var(--ink); }
</style>
</head>
<body>
<main class="canvas">

  <section class="label label--blue" aria-label="Merevaik rum label, blue edition">
    <svg viewBox="0 0 268 344" xmlns="http://www.w3.org/2000/svg">
      <defs>
        <linearGradient id="panel-shade-blue" x1="0" y1="0" x2="0" y2="1">
          <stop offset="0" stop-color="#3b3b3b"/>
          <stop offset="0.72" stop-color="#3b3b3b"/>
          <stop offset="1" stop-color="#a3a3a3"/>
        </linearGradient>
        <radialGradient id="scene-tone-blue" cx="0.5" cy="0.5" r="0.5">
          <stop offset="0" stop-color="#f2f2f2"/>
          <stop offset="1" stop-color="#c9c9c9" stop-opacity="0.7"/>
        </radialGradient>
      </defs>
      <rect class="accent-fill" x="0" y="0" width="268" height="344"/>
      <rect class="outer-rule" x="7.5" y="7.5" width="253" height="320" fill="none" stroke="#fff" stroke-width="1.2"/>
      <rect class="panel" x="12" y="12" width="244" height="292" fill="url(#panel-shade-blue)"/>
      <g class="oval-frame">
        <ellipse cx="134" cy="178" rx="113" ry="122" stroke-width="1.6"/>
        <ellipse cx="134" cy="178" rx="104" ry="113" stroke-width="1"/>
      </g>
      <circle class="brand-dot" cx="134" cy="40" r="13" fill="#fff"/>
      <text class="brand-name" x="134" y="118" text-anchor="middle">MEREVAIK</text>
      <line class="brand-rule" x1="80" y1="126" x2="188" y2="126" stroke="#fff" stroke-width="0.9"/>
      <text class="brand-sub" x="135.5" y="140" text-anchor="middle">DISTILLERY</text>
      <ellipse class="ship-scene" role="img" aria-label="Sailing ship with a pirate flag on rolling waves, seabirds overhead" cx="136" cy="222" rx="52" ry="58" fill="url(#scene-tone-blue)"/>
      <path class="wave-band accent-fill" d="M12 300 C 45 286, 80 306, 118 296 S 190 282, 222 294 S 248 300, 256 292 L256 344 L12 344 Z"/>
      <rect class="side-rule" x="7" y="290" width="1.2" height="38" fill="#fff"/>
      <rect class="side-rule" x="259.8" y="290" width="1.2" height="38" fill="#fff"/>
      <text class="spec" x="84" y="306" text-anchor="middle">vol.45%</text>
      <text class="spec" x="192" y="306" text-anchor="middle">750ml</text>
      <line class="spec-rule" x1="42" y1="314" x2="226" y2="314" stroke="#333" stroke-width="1"/>
      <line class="spec-rule" x1="110" y1="314" x2="158" y2="314" stroke="#333" stroke-width="2.4"/>
      <text class="origin-line" x="134" y="334" text-anchor="middle">RUM DISTILLERY IN <tspan class="origin-country">ESTONIA</tspan></text>
    </svg>
  </section>

  <section class="label label--red" aria-label="Merevaik rum label, red edition">
    <svg viewBox="0 0 268 344" xmlns="http://www.w3.org/2000/svg">
      <defs>
        <linearGradient id="panel-shade-red" x1="0" y1="0" x2="0" y2="1">
          <stop offset="0" stop-color="#3b3b3b"/>
          <stop offset="0.72" stop-color="#3b3b3b"/>
          <stop offset="1" stop-color="#a3a3a3"/>
        </linearGradient>
        <radialGradient id="scene-tone-red" cx="0.5" cy="0.5" r="0.5">
          <stop offset="0" stop-color="#f2f2f2"/>
          <stop offset="1" stop-color="#c9c9c9" stop-opacity="0.7"/>
        </radialGradient>
      </defs>
      <rect class="accent-fill" x="0" y="0" width="268" height="344"/>
      <rect class="outer-rule" x="7.5" y="7.5" width="253" height="320" fill="none" stroke="#fff" stroke-width="1.2"/>
      <rect class="panel" x="12" y="12" width="244" height="292" fill="url(#panel-shade-red)"/>
      <g class="oval-frame">
        <ellipse cx="134" cy="178" rx="113" ry="122" stroke-width="1.6"/>
        <ellipse cx="134" cy="178" rx="104" ry="113" stroke-width="1"/>
      </g>
      <circle class="brand-dot" cx="134" cy="40" r="13" fill="#fff"/>
      <text class="brand-name" x="134" y="118" text-anchor="middle">MEREVAIK</text>
      <line class="brand-rule" x1="80" y1="126" x2="188" y2="126" stroke="#fff" stroke-width="0.9"/>
      <text class="brand-sub" x="135.5" y="140" text-anchor="middle">DISTILLERY</text>
      <ellipse class="ship-scene" role="img" aria-label="Sailing ship with a pirate flag on rolling waves, seabirds overhead" cx="136" cy="222" rx="52" ry="58" fill="url(#scene-tone-red)"/>
      <path class="wave-band accent-fill" d="M12 300 C 45 286, 80 306, 118 296 S 190 282, 222 294 S 248 300, 256 292 L256 344 L12 344 Z"/>
      <rect class="side-rule" x="7" y="290" width="1.2" height="38" fill="#fff"/>
      <rect class="side-rule" x="259.8" y="290" width="1.2" height="38" fill="#fff"/>
      <text class="spec" x="84" y="306" text-anchor="middle">vol.45%</text>
      <text class="spec" x="192" y="306" text-anchor="middle">750ml</text>
      <line class="spec-rule" x1="42" y1="314" x2="226" y2="314" stroke="#333" stroke-width="1"/>
      <line class="spec-rule" x1="110" y1="314" x2="158" y2="314" stroke="#333" stroke-width="2.4"/>
      <text class="origin-line" x="134" y="334" text-anchor="middle">RUM DISTILLERY IN <tspan class="origin-country">ESTONIA</tspan></text>
    </svg>
  </section>

</main>
</body>
</html>
```